Design profile for Tapetix Nordvale

I had a logo competition here recently, and was left with two logos that I could not choose between. Therefore, I create this competition where I want a complete design package or a visual identity for the company. I want you to create design elements that can be used both in print and online. (letterhead, envelopes, business card, website, chatterloop, etc.) I have also attached a picture of the car I have ordered. I'm happy if you can show how the design can be used on that as well.
What is important is that the logos are treated individually, and that the design you create reflects or builds up under the logo. I want the design to be recognizable and to have a connection with the logo and what we do. (take fizzo lumba as an example. if you remove the name, but keep the red color and the white line, then you will recognize which brand it is about right away)
You choose whether you want to make proposals only for one logo, or or both, but it is important that they are treated individually. The best overall package determines which logo I use.
I have also added an image that you can use as an example background if you want it in a chatterloop banner for example.
It is important that the design looks professional and unique. A number of designs have come in, but many of the designs are very similar and general. Here is a video of the printer if you need inspiration: https://clipvaultia.net/Xr9TbLq2WsE

Industry/Entity Type

WallPrinting

Requirements
Must have
• Unique an professional design that can be used both online and print
Nice to have
• Show how to use the design on a KV Trolle. (see photos attached)
Should not have
• The design can be simple, but not too simple and general. I want it to give the company an identity

```html
<!DOCTYPE html>
<html lang="en">
<head>
<meta charset="utf-8">
<title>Tapetix Nordvale — Business Card</title>
<link rel="stylesheet" href="https://fonts.googleapis.com/css2?family=Montserrat:wght@600;700&family=Roboto:wght@400&display=swap">
<style>
  :root {
    --backdrop: #1b1b1d;
    --card: #f4f4f4;
    --ink: #1d1d1f;
    --text-grey: #6a6a6a;
    --accent-red: #e8343f;
    --divider-blue: #3f63a8;
  }
  * { margin: 0; padding: 0; box-sizing: border-box; }
  html, body {
    width: 1200px; height: 900px; overflow: hidden;
    background: var(--backdrop);
  }
  .stage {
    width: 1200px; height: 900px;
    display: flex; align-items: center; justify-content: center;
  }
  .business-card {
    width: 980px; height: 560px;
    background: var(--card);
    position: relative;
    display: flex; align-items: center;
    box-shadow: 0 20px 50px rgba(0,0,0,.5);
  }
  .brand {
    width: 520px;
    display: flex; align-items: center; justify-content: center; gap: 16px;
  }
  .brand-square {
    width: 26px; height: 26px;
    background: var(--ink);
  }
  .brand-name {
    font-family: "Montserrat", sans-serif;
    font-weight: 700;
    font-size: 40px;
    color: var(--ink);
    letter-spacing: -0.5px;
  }
  .divider {
    width: 2px; height: 300px;
    background: var(--divider-blue);
  }
  .contact {
    padding-left: 44px;
    font-family: "Roboto", sans-serif;
    color: var(--text-grey);
  }
  .person-name {
    font-family: "Montserrat", sans-serif;
    font-weight: 700;
    font-size: 27px;
    letter-spacing: 1.5px;
    text-transform: uppercase;
    color: var(--ink);
    line-height: 1.1;
  }
  .person-role {
    font-family: "Roboto", sans-serif;
    font-size: 25px;
    color: var(--accent-red);
    margin-bottom: 22px;
  }
  .address {
    font-style: normal;
    font-size: 22px;
    line-height: 1.35;
    margin-bottom: 14px;
  }
  .channels { list-style: none; font-size: 22px; line-height: 1.4; }
  .channels li { display: flex; align-items: center; gap: 10px; }
  .channels svg { width: 20px; height: 20px; flex: none; }
  .icon { fill: none; stroke: var(--accent-red); stroke-width: 2; }
  .icon-fill { fill: var(--accent-red); }
</style>
</head>
<body>
<main class="stage">
  <section class="business-card">
    <div class="brand">
      <span class="brand-square"></span>
      <span class="brand-name">Tapetix Nordvale</span>
    </div>
    <div class="divider"></div>
    <div class="contact">
      <h1 class="person-name">Henrik Aldermann</h1>
      <p class="person-role">Founder &amp; CEO</p>
      <address class="address">
        Tapetix-Nordvale<br>
        14 Marlow Creek Road<br>
        Ashford Vale, ON K7R 3P4
      </address>
      <ul class="channels">
        <li>
          <svg viewBox="0 0 20 20" aria-hidden="true"><path class="icon-fill" d="M5 2l3 4-2 2c1 2.5 3.5 5 6 6l2-2 4 3-2 3C9 17 3 11 2 4z"/></svg>
          555-318-2740
        </li>
        <li>
          <svg viewBox="0 0 20 20" aria-hidden="true"><rect class="icon-fill" x="1" y="4" width="18" height="12"/><path d="M1 4l9 7 9-7" fill="none" stroke="#f4f4f4" stroke-width="1.6"/></svg>
          info@tapetixpost.com
        </li>
        <li>
          <svg viewBox="0 0 20 20" aria-hidden="true"><circle class="icon" cx="10" cy="10" r="8"/><ellipse class="icon" cx="10" cy="10" rx="3.5" ry="8"/><path class="icon" d="M2 10h16"/></svg>
          www.tapetixhub.com
        </li>
      </ul>
    </div>
  </section>
</main>
</body>
</html>
```